Digital One Pager for Consulting Practice

I would like the essence of the content in my ppt consolidated into a one-pager. The one-pager will mainly be sent via email as a pdf and intended to excite and invite new clients and establish the credibility of my boutique high-end consulting firm. Infographics and symbols would be a plus. The target client should view the firm as providing premeir service. The client is getting a thought partner.

Target Market(s)

Large Medical Device Manufacturer Executives, Early-Stage Medical Device Manufacturer Executives, Partners at VC Firms

Industry/Entity Type

Medical Equipment

Colors
0355a3
f37122

Requirements
Must have
• Please match the color scheme in ppt. Please use the existing logo. I am very open to better graphics on the process. My photo does not need to be on the digital flyer. Hyper link to the website and email is needed.
Nice to have
• Infographics

```html
<!DOCTYPE html>
<html lang="en">
<head>
<meta charset="utf-8">
<title>Kestrel Ridge – Regulatory Consulting One Pager</title>
<link href="https://fonts.googleapis.com/css2?family=Carlito:wght@400;700&family=Tinos&family=Open+Sans:wght@400;600&display=swap" rel="stylesheet">
<style>
  :root {
    --navy: #111c35;
    --orange: #f37122;
    --panel: #f2f2f2;
    --grey-text: #7a7a7a;
    --ink: #1e2a44;
    --white: #ffffff;
  }
  * { box-sizing: border-box; margin: 0; padding: 0; }
  html, body { width: 956px; height: 1200px; overflow: hidden; background: var(--white); }
  .page { position: relative; width: 956px; height: 1200px; font-family: "Open Sans", sans-serif; }

  .masthead { position: absolute; left: 0; top: 0; width: 956px; height: 164px; background: var(--white); }
  .brand { position: absolute; left: 28px; top: 52px; display: flex; align-items: center; gap: 14px; }
  .brand-mark { width: 26px; height: 26px; border-radius: 50%; background: var(--navy); }
  .brand-name { font-family: "Carlito", sans-serif; font-weight: 700; font-size: 50px; letter-spacing: 5px; color: var(--navy); line-height: 1; }

  .value-band { position: absolute; left: 0; top: 164px; width: 956px; height: 267px; background: var(--navy); }
  .value-title { position: absolute; left: 28px; top: 48px; font-family: "Tinos", serif; font-size: 52px; color: var(--orange); line-height: 1; }
  .value-list { list-style: none; position: absolute; top: 118px; display: grid; row-gap: 12px; }
  .value-list.col-a { left: 28px; }
  .value-list.col-b { left: 526px; }
  .value-list li { display: flex; align-items: center; gap: 16px; font-family: "Carlito", sans-serif; font-size: 38px; color: var(--white); line-height: 44px; }
  .value-list svg { width: 28px; height: 28px; flex: none; }

  .services { position: absolute; left: 0; top: 431px; width: 507px; height: 687px; background: var(--white); }
  .services svg { width: 507px; height: 687px; display: block; }

  .offer-panel { position: absolute; left: 507px; top: 431px; width: 449px; height: 687px; background: var(--panel); }
  .offer-panel > * { position: absolute; }
  .section-heading { left: 30px; font-family: "Tinos", serif; font-size: 26px; color: var(--orange); line-height: 1; }
  .sub-heading { left: 28px; font-family: "Carlito", sans-serif; font-size: 17px; color: var(--ink); }
  .bullet { left: 28px; width: 400px; display: flex; gap: 12px; font-family: "Carlito", sans-serif; font-size: 16.5px; line-height: 21px; color: var(--grey-text); }
  .bullet svg { width: 15px; height: 15px; flex: none; margin-top: 3px; }

  .process-steps { left: 18px; top: 416px; width: 420px; display: flex; justify-content: space-between; }
  .step { width: 100px; text-align: center; }
  .step-icon { width: 64px; height: 64px; margin: 0 auto; border-radius: 50%; background: var(--orange); box-shadow: 0 6px 6px -3px rgba(0,0,0,.25); display: flex; align-items: center; justify-content: center; }
  .step-icon svg { width: 34px; height: 34px; }
  .step-label { margin-top: 14px; font-family: "Carlito", sans-serif; font-size: 12px; line-height: 14px; color: var(--grey-text); text-transform: uppercase; }

  .partner-row { left: 28px; display: flex; align-items: center; gap: 8px; }
  .badge { background: #cfd3da; border-radius: 2px; }
  .badge.dark { background: #3b4256; }
  .badge.blue { background: #1f5fae; }

  .contact-bar { position: absolute; left: 0; top: 1118px; width: 956px; height: 82px; display: flex; }
  .phone-block { width: 457px; background: var(--orange); display: flex; align-items: center; justify-content: center; gap: 18px; color: var(--white); font-family: "Open Sans", sans-serif; font-size: 36px; }
  .phone-block svg { width: 34px; height: 34px; }
  .web-block { flex: 1; background: var(--navy); display: flex; align-items: center; justify-content: center; gap: 10px; font-family: "Open Sans", sans-serif; font-size: 17.5px; color: var(--white); }
  .web-block a { color: var(--white); text-decoration: none; }
</style>
</head>
<body>
<main class="page">

  <header class="masthead">
    <div class="brand">
      <span class="brand-mark"></span>
      <span class="brand-name">KESTREL RIDGE</span>
    </div>
  </header>

  <section class="value-band">
    <h1 class="value-title">VALUE</h1>
    <ul class="value-list col-a">
      <li><svg viewBox="0 0 28 28"><rect x="2" y="4" width="20" height="20" rx="4" fill="none" stroke="#f37122" stroke-width="2.6"/><path d="M8 13l5 5L26 4" fill="none" stroke="#f37122" stroke-width="2.8" stroke-linecap="round" stroke-linejoin="round"/></svg>Extensive Experience</li>
      <li><svg viewBox="0 0 28 28"><rect x="2" y="4" width="20" height="20" rx="4" fill="none" stroke="#f37122" stroke-width="2.6"/><path d="M8 13l5 5L26 4" fill="none" stroke="#f37122" stroke-width="2.8" stroke-linecap="round" stroke-linejoin="round"/></svg>Efficient Process</li>
    </ul>
    <ul class="value-list col-b">
      <li><svg viewBox="0 0 28 28"><rect x="2" y="4" width="20" height="20" rx="4" fill="none" stroke="#f37122" stroke-width="2.6"/><path d="M8 13l5 5L26 4" fill="none" stroke="#f37122" stroke-width="2.8" stroke-linecap="round" stroke-linejoin="round"/></svg>Valued Network</li>
      <li><svg viewBox="0 0 28 28"><rect x="2" y="4" width="20" height="20" rx="4" fill="none" stroke="#f37122" stroke-width="2.6"/><path d="M8 13l5 5L26 4" fill="none" stroke="#f37122" stroke-width="2.8" stroke-linecap="round" stroke-linejoin="round"/></svg>Regulatory Strategy</li>
    </ul>
  </section>

  <section class="services" aria-label="Services">
    <svg viewBox="0 0 451 631" preserveAspectRatio="none">
      <g font-family="Open Sans, sans-serif" text-anchor="middle" stroke="none">
        <!-- regulatory strategy -->
        <polygon points="31,170 87,73 199,73 255,170 199,266 87,266" fill="#f37122" stroke="#fff" stroke-width="4"/>
        <!-- interim leadership -->
        <polygon points="31,364 87,267 199,267 255,364 199,461 87,461" fill="#111c35" stroke="#fff" stroke-width="4"/>
        <!-- fda communications -->
        <polygon points="201,267 257,171 369,171 425,267 369,364 257,364" fill="#f37122" stroke="#fff" stroke-width="4"/>
        <!-- training -->
        <polygon points="201,462 257,365 369,365 425,462 369,559 257,559" fill="#111c35" stroke="#fff" stroke-width="4"/>

        <!-- icon badges -->
        <circle cx="143" cy="96" r="31" fill="#fff"/>
        <circle cx="143" cy="96" r="26" fill="#f37122"/>
        <g fill="#fff"><rect x="129" y="99" width="5" height="12"/><rect x="137" y="94" width="5" height="17"/><rect x="145" y="89" width="5" height="22"/><rect x="153" y="84" width="5" height="27"/></g>
        <path d="M126 95 L138 84 L146 88 L159 76" fill="none" stroke="#fff" stroke-width="2.6"/>
        <path d="M153 75 L160 75 L160 82" fill="none" stroke="#fff" stroke-width="2.6"/>

        <circle cx="313" cy="195" r="31" fill="#fff"/>
        <circle cx="313" cy="195" r="26" fill="#f37122"/>
        <rect x="302" y="180" width="20" height="27" fill="#fff"/>
        <rect x="306" y="184" width="20" height="27" fill="#fff" stroke="#f37122" stroke-width="1.5"/>
        <g stroke="#f37122" stroke-width="1.5"><line x1="310" y1="191" x2="322" y2="191"/><line x1="310" y1="196" x2="322" y2="196"/><line x1="310" y1="201" x2="322" y2="201"/></g>

        <circle cx="143" cy="290" r="31" fill="#fff"/>
        <circle cx="143" cy="290" r="26" fill="#111c35"/>
        <g fill="#fff" stroke="#fff" stroke-width="2">
          <circle cx="143" cy="282" r="6"/>
          <line x1="143" y1="288" x2="143" y2="302"/>
          <line x1="128" y1="302" x2="158" y2="302"/>
          <circle cx="128" cy="302" r="3"/><circle cx="143" cy="305" r="3"/><circle cx="158" cy="302" r="3"/>
        </g>

        <circle cx="313" cy="390" r="31" fill="#fff"/>
        <circle cx="313" cy="390" r="26" fill="#111c35"/>
        <rect x="302" y="377" width="19" height="25" fill="none" stroke="#fff" stroke-width="2"/>
        <g stroke="#fff" stroke-width="1.8"><line x1="306" y1="384" x2="316" y2="384"/><line x1="306" y1="389" x2="316" y2="389"/><line x1="306" y1="394" x2="313" y2="394"/></g>
        <path d="M314 400 L326 386" stroke="#fff" stroke-width="3"/>

        <!-- labels -->
        <g fill="#fff">
          <text x="143" y="157" font-size="15.5">REGULATORY</text>
          <text x="143" y="179" font-size="15.5">STRATEGY</text>
          <text x="143" y="203" font-size="11.5">RAQA Organizational Structure</text>
          <text x="143" y="219" font-size="11.5">Regulatory Pathway</text>

          <text x="313" y="256" font-size="15.5">FDA</text>
          <text x="313" y="278" font-size="15.5">COMMUNICATIONS</text>
          <text x="313" y="303" font-size="11.5">Deficiency Response</text>
          <text x="313" y="319" font-size="11.5">Application Review</text>

          <text x="143" y="356" font-size="15.5">INTERIM</text>
          <text x="143" y="378" font-size="15.5">EXECUTIVE LEADERSHIP</text>
          <text x="143" y="406" font-size="11.5">Compliance Remediation</text>
          <text x="143" y="422" font-size="11.5">Accelerated Product</text>
          <text x="143" y="438" font-size="11.5">Registration</text>

          <text x="313" y="452" font-size="15.5">TRAINING</text>
          <text x="313" y="477" font-size="11.5">FDA Communication</text>
          <text x="313" y="493" font-size="11.5">MDR Reporting</text>
        </g>
      </g>
    </svg>
  </section>

  <section class="offer-panel">
    <h2 class="section-heading" style="top:54px">Experience to Provide...</h2>

    <h3 class="sub-heading" style="top:90px">Executive Application Review</h3>
    <p class="bullet" style="top:117px"><svg viewBox="0 0 15 15"><circle cx="7.5" cy="7.5" r="6.5" fill="none" stroke="#7a7a7a"/><path d="M6 4.5l3 3-3 3" fill="none" stroke="#7a7a7a" stroke-width="1.4"/></svg><span>Examples include: Presubmission, IDE, 510(k), 513(g), PMA, Refuse to Accept, Hold letter</span></p>
    <p class="bullet" style="top:177px"><svg viewBox="0 0 15 15"><circle cx="7.5" cy="7.5" r="6.5" fill="none" stroke="#7a7a7a"/><path d="M6 4.5l3 3-3 3" fill="none" stroke="#7a7a7a" stroke-width="1.4"/></svg><span>Troubleshooting</span></p>

    <h3 class="sub-heading" style="top:220px">Strategic Advice &amp; Diligence to Investors</h3>
    <p class="bullet" style="top:248px"><svg viewBox="0 0 15 15"><circle cx="7.5" cy="7.5" r="6.5" fill="none" stroke="#7a7a7a"/><path d="M6 4.5l3 3-3 3" fill="none" stroke="#7a7a7a" stroke-width="1.4"/></svg><span>Validate &amp; Verify Founder Milestones</span></p>
    <p class="bullet" style="top:281px"><svg viewBox="0 0 15 15"><circle cx="7.5" cy="7.5" r="6.5" fill="none" stroke="#7a7a7a"/><path d="M6 4.5l3 3-3 3" fill="none" stroke="#7a7a7a" stroke-width="1.4"/></svg><span>Diligence portfolio company Regulatory and Quality systems</span></p>

    <h2 class="section-heading" style="top:372px">Efficient Process</h2>

    <div class="process-steps">
      <div class="step">
        <div class="step-icon"><svg viewBox="0 0 34 34"><path d="M10 6c2-1 4 3 4 5s-3 2-2 5 4 6 6 7 3-2 5-2 5 3 4 5-3 4-6 3C14 27 7 19 6 12c0-3 2-5 4-6z" fill="#fff"/></svg></div>
        <p class="step-label">Exploratory<br>Call</p>
      </div>
      <div class="step">
        <div class="step-icon"><svg viewBox="0 0 34 34"><rect x="6" y="5" width="18" height="24" fill="none" stroke="#fff" stroke-width="2.2"/><g stroke="#fff" stroke-width="2"><line x1="10" y1="11" x2="20" y2="11"/><line x1="10" y1="16" x2="16" y2="16"/></g><circle cx="21" cy="21" r="5" fill="#f37122" stroke="#fff" stroke-width="2.2"/><line x1="25" y1="25" x2="30" y2="30" stroke="#fff" stroke-width="3"/></svg></div>
        <p class="step-label">Regulatory<br>Landscape</p>
      </div>
      <div class="step">
        <div class="step-icon"><svg viewBox="0 0 34 34"><path d="M17 4a9 9 0 0 0-5 16.5V24h10v-3.5A9 9 0 0 0 17 4z" fill="#fff"/><rect x="13" y="26" width="8" height="2.5" fill="#fff"/><rect x="14" y="30" width="6" height="2" fill="#fff"/></svg></div>
        <p class="step-label">Problem<br>Statement</p>
      </div>
      <div class="step">
        <div class="step-icon"><svg viewBox="0 0 34 34"><circle cx="13" cy="20" r="7" fill="none" stroke="#fff" stroke-width="5" stroke-dasharray="3 2.5"/><circle cx="13" cy="20" r="3" fill="#fff"/><circle cx="24" cy="10" r="5" fill="none" stroke="#fff" stroke-width="4" stroke-dasharray="2.5 2"/><circle cx="24" cy="10" r="2" fill="#fff"/></svg></div>
        <p class="step-label">Review &amp; Align<br>on Deliverables</p>
      </div>
    </div>

    <h3 class="sub-heading" style="top:571px">Valued Partner Network</h3>
    <div class="partner-row" style="top:593px">
      <span class="badge" style="width:214px;height:18px"></span>
      <span class="badge" style="width:44px;height:22px"></span>
      <span class="badge dark" style="width:62px;height:28px"></span>
    </div>
    <div class="partner-row" style="top:630px">
      <span class="badge" style="width:62px;height:24px"></span>
      <span class="badge blue" style="width:52px;height:26px"></span>
      <span class="badge" style="width:62px;height:24px"></span>
    </div>
  </section>

  <footer class="contact-bar">
    <div class="phone-block">
      <svg viewBox="0 0 34 34"><circle cx="17" cy="17" r="14.5" fill="none" stroke="#fff" stroke-width="2.4"/><path d="M12 9c1.4-.7 2.8 2 2.8 3.4s-2 1.4-1.4 3.4 2.8 4.2 4.2 4.8 2-1.4 3.4-1.4 3.4 2 2.8 3.4-2 2.8-4.2 2C15 23 11 18.5 10.5 14c0-2 .8-4.2 1.5-5z" fill="#fff"/></svg>
      <span>555.014.2280</span>
    </div>
    <div class="web-block">
      <a href="https://www.kestrelridge.com">www.kestrelridge.com</a>
      <span>|</span>
      <a href="mailto:info@kestrelridge.com">info@kestrelridge.com</a>
    </div>
  </footer>

</main>
</body>
</html>
```